Global Educational start-up needs elegant website

Hi,
I am looking for a website for a company which is serving the high-end, demanding clients in China, on educational market and working internationally. The company name is Copper Lantern Educational Services. Please find attached its logo.
We need a website consisting of seven sites:
1. What do we do? (main/basic site)
2. Programs (two subsites under this site)
a) Leadership, Entrepreneurship and Personal Development (Europe)
b) Career incubator (UK)
3. Our mission and values
4. Who are we?
5. Testimonials
6. Contact us
7. Sign for a program! (button redirecting to a form)
We would appreciate simplicity, elegance and minimalizm. It should be interactive and should meet highest expectations of the rich cusomers. On the visual materials the Chinese children aged 13-20 are preferred, in link with education, development and so on.
Time is short so we might finish the contest in a moment we find a proper choice.
Parents of rich Chinese children.
Education

```html
<!DOCTYPE html>
<html lang="en">
<head>
<meta charset="utf-8">
<title>Copper Lantern Educational Services</title>
<link href="https://fonts.googleapis.com/css2?family=Open+Sans:wght@400;600;700&family=Roboto+Condensed:wght@400;700&display=swap" rel="stylesheet">
<style>
:root{
  --green:#3fa535;
  --ink:#333333;
  --muted:#8a8a8a;
  --body-text:#666666;
  --grey-band:#f0f0f0;
  --black:#111111;
  --footer:#1b1b1b;
  --white:#ffffff;
}
*{box-sizing:border-box;margin:0;padding:0}
html,body{width:1200px;height:2293px;overflow:hidden;background:var(--white)}
body{font-family:"Open Sans",Arial,sans-serif;color:var(--ink);position:relative}
.heading{font-family:"Roboto Condensed",Arial,sans-serif;font-weight:400;text-transform:uppercase}

/* header */
.site-header{position:absolute;left:0;top:0;width:1200px;height:99px;background:var(--white)}
.brand-panel{position:absolute;left:0;top:0}
.brand{position:absolute;left:183px;top:28px;display:flex;align-items:center;gap:14px}
.brand-mark{width:40px;height:40px;border:2px solid #cfcfcf;border-radius:50%}
.brand-name{font-size:15px;line-height:19px;color:#cfcfcf;letter-spacing:1px;text-transform:uppercase}
.contact-strip{position:absolute;left:0;top:0;width:1200px;height:38px}
.contact-item{position:absolute;top:11px;font-size:11.5px;color:var(--white);display:flex;align-items:center;gap:7px}
.main-nav{position:absolute;top:54px;left:0;width:1200px;height:27px}
.main-nav a{position:absolute;top:0;height:27px;line-height:27px;font-size:11.5px;color:#444;text-decoration:none;text-transform:uppercase}
.main-nav a.active{background:var(--green);color:var(--white);padding:0 11px}

/* hero */
.hero{position:absolute;left:0;top:99px;width:1200px;height:473px;
  background:
    radial-gradient(ellipse 170px 90px at 600px 110px,rgba(110,100,80,.85),rgba(110,100,80,0) 100%),
    radial-gradient(ellipse 120px 110px at 605px 200px,rgba(120,90,70,.9),rgba(120,90,70,0) 100%),
    radial-gradient(ellipse 260px 170px at 580px 420px,rgba(140,165,140,.95),rgba(140,165,140,0) 100%),
    radial-gradient(ellipse 220px 60px at 590px 260px,rgba(150,155,120,.7),rgba(150,155,120,0) 100%),
    radial-gradient(ellipse 300px 260px at 180px 200px,rgba(80,120,50,.8),rgba(80,120,50,0) 100%),
    radial-gradient(ellipse 300px 260px at 1020px 220px,rgba(90,130,55,.8),rgba(90,130,55,0) 100%),
    linear-gradient(180deg,#2c4020 0%,#1f3118 55%,#233a1a 100%)}
.slider-arrow{position:absolute;top:193px;width:34px;height:34px}

/* features */
.features{position:absolute;left:0;top:572px;width:1200px;height:252px}
.feature{position:absolute;top:44px;width:200px;text-align:center}
.feature-title{font-size:16px;color:#444;margin-top:8px}
.feature-title.accent{color:var(--green)}
.feature-text{font-size:10.5px;line-height:18px;color:var(--muted);margin-top:5px}

/* bands */
.band{position:absolute;left:0;width:1200px}
.band.grey{background:var(--grey-band)}
.section-title{position:absolute;left:0;width:1200px;text-align:center;font-size:19.5px;color:var(--green)}
.section-rule{position:absolute;left:543px;width:114px;height:2px;background:var(--green)}
.section-copy{position:absolute;left:176px;width:848px;text-align:center;font-size:12.8px;line-height:24.5px;color:var(--body-text)}
.more-circle{position:absolute;left:584px;width:32px;height:32px}

/* programs */
.program{position:absolute;top:94px;width:194px;text-align:center}
.program-photo{width:194px;height:187px}
.program-title{font-size:16px;color:#444;margin-top:12px}
.program-title.accent{color:var(--green)}
.program-text{font-size:9.8px;line-height:17px;color:#999;margin-top:3px}
.program-more{display:flex;justify-content:center;align-items:center;gap:10px;margin-top:10px;font-size:10.5px;color:#999}
.program-more .bar{width:1px;height:20px;background:#999}
.plus{width:20px;height:20px;border:1.5px solid var(--green);border-radius:50%;display:flex;align-items:center;justify-content:center;color:var(--green);font-size:13px;line-height:1}

/* contact */
.contact{position:absolute;left:0;top:1729px;width:1200px;height:405px;
  background:
    radial-gradient(ellipse 180px 200px at 680px 90px,rgba(95,70,60,.9),rgba(95,70,60,0) 100%),
    radial-gradient(ellipse 260px 170px at 860px 260px,rgba(150,60,85,.75),rgba(150,60,85,0) 100%),
    radial-gradient(ellipse 220px 140px at 640px 330px,rgba(120,105,100,.6),rgba(120,105,100,0) 100%),
    linear-gradient(100deg,#2c2c2c 0%,#3a3636 35%,#3e3434 60%,#302e2e 80%,#262626 100%)}
.contact-shade{position:absolute;inset:0;background:rgba(20,20,20,.3)}
.field{position:absolute;border-bottom:1px solid #9a9a9a;height:30px;font-size:11.5px;color:#dddddd;padding:0 0 8px 18px;display:flex;align-items:flex-end}
.field.area{border:1px solid #9a9a9a;align-items:flex-start;padding:14px 16px}
.send-btn{position:absolute;left:555px;top:335px;width:89px;height:35px;background:var(--green);color:var(--white);font-family:"Roboto Condensed",Arial,sans-serif;font-weight:700;font-size:17px;letter-spacing:1px;text-align:center;line-height:35px}

/* newsletter */
.newsletter{position:absolute;left:0;top:2134px;width:1200px;height:92px;background:#efefef}
.news-title{position:absolute;left:183px;top:26px;font-family:"Roboto Condensed",Arial,sans-serif;font-weight:700;font-size:15.5px;color:#222;text-transform:uppercase}
.news-sub{position:absolute;left:183px;top:52px;font-size:13px;font-weight:600;color:#222}
.news-sub span{color:var(--green)}
.news-input{position:absolute;left:662px;top:26px;width:242px;height:40px;background:var(--white);font-size:11.5px;color:#555;padding:0 16px;line-height:40px}
.news-btn{position:absolute;left:904px;top:26px;width:113px;height:40px;background:var(--green);color:var(--white);font-weight:700;font-size:14.5px;letter-spacing:.5px;text-align:center;line-height:40px;text-transform:uppercase}

/* footer */
.site-footer{position:absolute;left:0;top:2226px;width:1200px;height:67px;background:var(--footer)}
.footer-links{position:absolute;left:183px;top:15px;font-size:11.5px;color:#bbbbbb}
.footer-links .current{color:var(--green)}
.copyright{position:absolute;left:183px;top:40px;font-size:10.5px;color:#aaaaaa}
.copyright span{color:var(--green)}
.social{position:absolute;top:19px;width:30px;height:30px;border-radius:50%;border:1.5px solid #8a8a8a;background:#2a2a2a}
.social.first{background:var(--green);border-color:var(--green)}
</style>
</head>
<body>

<header class="site-header">
  <svg class="brand-panel" width="1200" height="99" viewBox="0 0 1200 99" aria-hidden="true">
    <rect x="0" y="0" width="1200" height="38" fill="#3fa535"/>
    <path d="M0 0 H535 L505 88 Q500 99 485 99 H0 Z" fill="#111111"/>
  </svg>
  <div class="brand">
    <div class="brand-mark"></div>
    <div class="brand-name">Copper Lantern<br>Educational Services</div>
  </div>
  <div class="contact-strip">
    <div class="contact-item" style="left:758px">
      <svg width="13" height="13" viewBox="0 0 24 24" aria-hidden="true"><path d="M6.6 10.8a15 15 0 0 0 6.6 6.6l2.2-2.2a1 1 0 0 1 1-.25 11.4 11.4 0 0 0 3.6.57 1 1 0 0 1 1 1V20a1 1 0 0 1-1 1A17 17 0 0 1 3 4a1 1 0 0 1 1-1h3.5a1 1 0 0 1 1 1c0 1.25.2 2.45.57 3.57a1 1 0 0 1-.25 1z" fill="#111"/></svg>
      555-014-2290
    </div>
    <div class="contact-item" style="left:873px">
      <svg width="14" height="12" viewBox="0 0 24 20" aria-hidden="true"><rect x="1" y="2" width="22" height="16" fill="#111"/><path d="M1 2 L12 11 L23 2" stroke="#3fa535" stroke-width="2" fill="none"/></svg>
      hello@copperlantern-edu.com
    </div>
  </div>
  <nav class="main-nav">
    <a class="active" style="left:538px">Home</a>
    <a style="left:609px">Courses</a>
    <a style="left:686px">About</a>
    <a style="left:751px">Teachers</a>
    <a style="left:833px">Blog</a>
    <a style="left:891px">Gallery</a>
    <a style="left:965px">Contact</a>
  </nav>
</header>

<section class="hero" role="img" aria-label="Hero photograph: a man in a hat standing in a green forest">
  <svg class="slider-arrow" style="left:150px" viewBox="0 0 34 34" aria-hidden="true"><circle cx="17" cy="17" r="15.5" fill="none" stroke="#fff" stroke-width="2"/><path d="M21 17H12M15.5 13.5L12 17l3.5 3.5" stroke="#fff" stroke-width="2" fill="none"/></svg>
  <svg class="slider-arrow" style="left:1017px" viewBox="0 0 34 34" aria-hidden="true"><circle cx="17" cy="17" r="15.5" fill="none" stroke="#fff" stroke-width="2"/><path d="M13 17h9M18.5 13.5L22 17l-3.5 3.5" stroke="#fff" stroke-width="2" fill="none"/></svg>
</section>

<section class="features">
  <div class="feature" style="left:166px">
    <svg width="84" height="92" viewBox="0 0 84 92" aria-hidden="true">
      <circle cx="42" cy="42" r="40" fill="#fff" stroke="#3fa535" stroke-width="1.5"/>
      <path d="M36 82 L42 90 L48 82" fill="#3fa535"/>
      <circle cx="42" cy="42" r="36" fill="#3fa535"/>
      <circle cx="40" cy="44" r="17" fill="none" stroke="#fff" stroke-width="3"/>
      <circle cx="40" cy="44" r="10" fill="none" stroke="#fff" stroke-width="3"/>
      <circle cx="40" cy="44" r="3.5" fill="#fff"/>
      <path d="M40 44 L58 26 M53 24 L60 24 L60 31" stroke="#fff" stroke-width="3" fill="none"/>
    </svg>
    <div class="feature-title heading accent">Our Mission</div>
    <div class="feature-text">Lorem ipsum dolor sit amet,<br>consectetur adipiscing elit.<br>Pellentesque rutrum .</div>
  </div>
  <div class="feature" style="left:389px">
    <svg width="84" height="92" viewBox="0 0 84 92" aria-hidden="true">
      <circle cx="42" cy="42" r="40" fill="#fff" stroke="#666" stroke-width="1.5"/>
      <path d="M36 82 L42 90 L48 82" fill="#666"/>
      <circle cx="42" cy="42" r="36" fill="#666"/>
      <path d="M18 38 L30 32 L42 36 L54 32 L66 38 L58 50 L48 56 L38 54 L26 46 Z" fill="#fff"/>
      <path d="M34 44 L42 50 M38 40 L47 47 M44 38 L52 44" stroke="#666" stroke-width="2"/>
    </svg>
    <div class="feature-title heading">Our Values</div>
    <div class="feature-text">Lorem ipsum dolor sit amet,<br>consectetur adipiscing elit.<br>Pellentesque.</div>
  </div>
  <div class="feature" style="left:614px">
    <svg width="84" height="92" viewBox="0 0 84 92" aria-hidden="true">
      <circle cx="42" cy="42" r="40" fill="#fff" stroke="#666" stroke-width="1.5"/>
      <path d="M36 82 L42 90 L48 82" fill="#666"/>
      <circle cx="42" cy="42" r="36" fill="#666"/>
      <rect x="27" y="28" width="28" height="28" rx="3" fill="none" stroke="#fff" stroke-width="3"/>
      <path d="M33 42 L40 49 L56 30" stroke="#fff" stroke-width="3.5" fill="none"/>
    </svg>
    <div class="feature-title heading">High-Quality</div>
    <div class="feature-text">Lorem ipsum dolor sit amet,<br>consectetur adipiscing elit.<br>Pellentesque rutrum.</div>
  </div>
  <div class="feature" style="left:837px">
    <svg width="84" height="92" viewBox="0 0 84 92" aria-hidden="true">
      <circle cx="42" cy="42" r="40" fill="#fff" stroke="#666" stroke-width="1.5"/>
      <path d="M36 82 L42 90 L48 82" fill="#666"/>
      <circle cx="42" cy="42" r="36" fill="#666"/>
      <path d="M16 36 L42 26 L68 36 L42 46 Z" fill="#fff"/>
      <path d="M28 41 V52 Q42 60 56 52 V41 L42 46 Z" fill="#fff"/>
      <path d="M64 37 V50" stroke="#fff" stroke-width="2"/>
    </svg>
    <div class="feature-title heading">Educational</div>
    <div class="feature-text">Lorem ipsum dolor sit amet,<br>consectetur adipiscing elit.<br>Pellentes.</div>
  </div>
</section>

<section class="band grey" style="top:824px;height:239px">
  <h2 class="section-title heading" style="top:29px">What do we do</h2>
  <div class="section-rule" style="top:62px"></div>
  <p class="section-copy" style="top:84px">Lorem ipsum dolor sit amet, consectetur adipiscing elit. Nulla leo nulla, pulvinar at convallis vitae, ultricies sed orci. Mauris eget magna arcu. Sed nulla ipsum, facilisis congue tempus at, suscipit sit amet nisi. Aenean sed elit sapien. Pellentesque rutrum mi ut nulla semper varius. Sed porta erat eu ornare faucibus. Sed tincidunt, lectus nec semper molestie, augue velit cursus felis,</p>
  <svg class="more-circle" style="top:175px" viewBox="0 0 32 32" aria-hidden="true"><circle cx="16" cy="16" r="14.5" fill="none" stroke="#3fa535" stroke-width="1.5"/><path d="M13.5 10 L19.5 16 L13.5 22" stroke="#3fa535" stroke-width="2" fill="none"/></svg>
</section>

<section class="band" style="top:1063px;height:420px">
  <h2 class="section-title heading" style="top:28px">Programs</h2>
  <div class="section-rule" style="top:66px"></div>
  <div class="program" style="left:183px">
    <div class="program-photo" role="img" aria-label="Photograph: a businessman presenting in a bright office" style="background:radial-gradient(ellipse 55px 80px at 95px 120px,rgba(200,195,175,.95),rgba(200,195,175,0) 100%),radial-gradient(ellipse 60px 40px at 95px 180px,rgba(140,150,160,.8),rgba(140,150,160,0) 100%),linear-gradient(100deg,#c9d2dc 0%,#e6eaee 45%,#f4f5f6 70%,#dde2e6 100%)"></div>
    <div class="program-title heading accent">Leadership</div>
    <div class="program-text">Lorem ipsum dolor sit amensectetur<br>adipiscing elitulla leo nulla pulvinar</div>
    <div class="program-more"><span class="bar"></span>More<span class="plus">+</span></div>
  </div>
  <div class="program" style="left:396px">
    <div class="program-photo" role="img" aria-label="Photograph: two businesswomen shaking hands" style="background:radial-gradient(ellipse 60px 90px at 45px 130px,rgba(40,36,36,.9),rgba(40,36,36,0) 100%),radial-gradient(ellipse 55px 90px at 150px 130px,rgba(240,240,240,.95),rgba(240,240,240,0) 100%),radial-gradient(ellipse 50px 60px at 150px 40px,rgba(90,70,60,.8),rgba(90,70,60,0) 100%),linear-gradient(160deg,#f2f2ef 0%,#e4e2dc 50%,#cfccc4 100%)"></div>
    <div class="program-title heading">Entrepreneurship</div>
    <div class="program-text">Lorem ipsum dolor sit amensectetur<br>adipiscing elitulla leo nulla pulvinar</div>
    <div class="program-more"><span class="bar"></span>More<span class="plus">+</span></div>
  </div>
  <div class="program" style="left:609px">
    <div class="program-photo" role="img" aria-label="Photograph: a student studying at a desk" style="background:radial-gradient(ellipse 60px 60px at 95px 70px,rgba(230,200,140,.9),rgba(230,200,140,0) 100%),radial-gradient(ellipse 75px 45px at 90px 140px,rgba(200,60,60,.75),rgba(200,60,60,0) 100%),linear-gradient(180deg,#f5f5f5 0%,#ececea 60%,#e0e2e4 100%)"></div>
    <div class="program-title heading">Personal Development</div>
    <div class="program-text">Lorem ipsum dolor sit amensectetur<br>adipiscing elitulla leo nulla pulvinar</div>
    <div class="program-more"><span class="bar"></span>More<span class="plus">+</span></div>
  </div>
  <div class="program" style="left:821px">
    <div class="program-photo" role="img" aria-label="Photograph: two students working at a laptop" style="background:radial-gradient(ellipse 60px 90px at 55px 90px,rgba(120,80,55,.9),rgba(120,80,55,0) 100%),radial-gradient(ellipse 55px 60px at 130px 150px,rgba(130,60,160,.85),rgba(130,60,160,0) 100%),radial-gradient(ellipse 40px 50px at 140px 60px,rgba(110,70,50,.8),rgba(110,70,50,0) 100%),linear-gradient(160deg,#b8c6d2 0%,#d6dde3 55%,#e8ecef 100%)"></div>
    <div class="program-title heading">Career Incubator</div>
    <div class="program-text">Lorem ipsum dolor sit amensectetur<br>adipiscing elitulla leo nulla pulvinar</div>
    <div class="program-more"><span class="bar"></span>More<span class="plus">+</span></div>
  </div>
</section>

<section class="band grey" style="top:1483px;height:246px">
  <h2 class="section-title heading" style="top:20px">Who we are</h2>
  <div class="section-rule" style="top:54px"></div>
  <p class="section-copy" style="top:94px">Lorem ipsum dolor sit amet, consectetur adipiscing elit. Nulla leo nulla, pulvinar at convallis vitae, ultricies sed orci. Mauris eget magna arcu. Sed nulla ipsum, facilisis congue tempus at, suscipit sit amet nisi. Aenean sed elit sapien. Pellentesque rutrum mi ut nulla semper varius. Sed porta erat eu ornare faucibus. Sed tincidunt, lectus nec semper molestie, augue velit cursus felis,</p>
  <svg class="more-circle" style="top:174px" viewBox="0 0 32 32" aria-hidden="true"><circle cx="16" cy="16" r="14.5" fill="none" stroke="#3fa535" stroke-width="1.5"/><path d="M13.5 10 L19.5 16 L13.5 22" stroke="#3fa535" stroke-width="2" fill="none"/></svg>
</section>

<section class="contact" role="img" aria-label="Background photograph: a student writing at a desk, darkened">
  <div class="contact-shade"></div>
  <h2 class="section-title heading" style="top:21px">Contact us</h2>
  <div class="section-rule" style="top:52px"></div>
  <div class="field" style="left:183px;top:73px;width:834px">Your Name</div>
  <div class="field" style="left:183px;top:126px;width:400px">Your Email</div>
  <div class="field" style="left:617px;top:126px;width:400px">Your Phone</div>
  <div class="field area" style="left:183px;top:182px;width:834px;height:133px">Your Mesaage</div>
  <div class="send-btn">SEND</div>
</section>

<section class="newsletter">
  <div class="news-title">Join our newsletter!</div>
  <div class="news-sub">Sign for a program.<span>Get Our Newsletters!</span></div>
  <div class="news-input">your@email.com</div>
  <div class="news-btn">Subscribe</div>
</section>

<footer class="site-footer">
  <div class="footer-links"><span class="current">Home</span> &nbsp;/&nbsp; Courses &nbsp;/&nbsp; About &nbsp;/&nbsp; Teachers &nbsp;/&nbsp; Blog &nbsp;/&nbsp; Gallery &nbsp;/&nbsp; Contact</div>
  <div class="copyright">© 2014 &nbsp;<span>Copper Lantern educational services</span>. All Rights Resverd.</div>
  <div class="social first" style="left:812px"></div>
  <div class="social" style="left:855px"></div>
  <div class="social" style="left:899px"></div>
  <div class="social" style="left:942px"></div>
  <div class="social" style="left:986px"></div>
</footer>

</body>
</html>
```